Artificial intelligence, machine learning, and automation company needs a sexy business card design

We need a sleek and sexy business card design for an AI consulting company based in Philadelphia PA. We provide custom machine learning and automation solutions for companies of all shapes and sizes. The primary industries that we serve are pharmaceuticals, engineering, healthcare, and computer software. We would like the designs to be a black business card that uses green as a sleek accent color. The final design should communicate intelligence, cutting edge new-tech, and optimization.

Target Market(s)

C-level and VP level executives of multi-million annual companies. Mostly in Pharma, Healthcare, Real Estate, Retail, and Engineering

Industry/Entity Type

Computer Software

Contact Information for Business Card

Name: Jack Moss
Title: CEO
Cell: 215 604 8293
Email: JackM@quillarcworks.example
Website: www.QuillarcWorks.example

Font styles to use
Sans Serif

Colors

Designer to choose colors to be used in the design.

Requirements
Must have
• 1) Attached Quillarc Logo (either with colors or not/embossed)
• 2) "Artificial Intelligence" "Automation" and "Machine Learning"
• 3) "Quillarc Laboratories" or "Quillarc Works" or "Quillarc"
• 4) Sexy AF.
Nice to have
• Black card / dark card color, "Quillarc Green" accent colors (in attached .ai file), Embossment of logo/name/etc, thick card stock, colored borders (on card sides, not front/back faces)
Should not have
• Should not be bland, or unsexy.

```html
<!DOCTYPE html>
<html lang="en">
<head>
<meta charset="utf-8">
<title>Quillarc Laboratories – Business Card</title>
<link href="https://fonts.googleapis.com/css2?family=Work+Sans:wght@400;500&display=swap" rel="stylesheet">
<style>
  :root {
    --backdrop: #2a2a2b;
    --card: #1e1e1f;
    --ink: #f4f4f4;
    --ink-soft: #d9d9d9;
    --accent: #ddc93a;
  }
  * { margin: 0; padding: 0; box-sizing: border-box; }
  html, body { width: 1200px; height: 900px; overflow: hidden; }
  body {
    background: var(--backdrop);
    font-family: "Work Sans", Arial, sans-serif;
    color: var(--ink);
    position: relative;
  }
  .card {
    position: absolute;
    left: 280px;
    width: 640px;
    height: 366px;
    background: linear-gradient(135deg, #1a1a1b 0%, #242425 60%, #2c2c2d 100%);
    overflow: hidden;
  }
  .card--back { top: 48px; }
  .card--front { top: 470px; }

  /* Back face */
  .brand-stack {
    position: absolute;
    left: 0; right: 0; top: 78px;
    display: flex; flex-direction: column; align-items: center;
  }
  .brand-square {
    width: 120px; height: 100px;
    border: 5px solid var(--ink);
    margin-bottom: 14px;
  }
  .brand-name {
    font-weight: 400;
    color: var(--ink);
    text-transform: uppercase;
    text-align: center;
    line-height: 1.2;
  }
  .brand-name--large .word-main { font-size: 28px; letter-spacing: 7px; display: block; }
  .brand-name--large .word-sub { font-size: 13px; letter-spacing: 4px; display: block; }
  .back-web {
    position: absolute; left: 0; right: 0; bottom: 42px;
    text-align: center; font-size: 15px; letter-spacing: .5px; color: var(--ink);
  }
  .back-web .highlight { color: var(--accent); }

  /* Front face */
  .brand-row {
    position: absolute; left: 40px; top: 36px;
    display: flex; align-items: center; gap: 12px;
  }
  .brand-row .brand-square { width: 66px; height: 52px; border-width: 3px; margin: 0; }
  .brand-name--small .word-main { font-size: 26px; letter-spacing: 6px; display: block; }
  .brand-name--small .word-sub { font-size: 13px; letter-spacing: 3.5px; display: block; text-align: left; }

  .divider {
    position: absolute; left: 90px; right: 50px; top: 232px;
    height: 1px; background: var(--accent);
  }
  .contact {
    position: absolute; left: 48px; top: 248px;
    list-style: none; font-size: 17px; line-height: 22px; color: var(--ink);
  }
  .contact li { display: flex; align-items: center; gap: 10px; }
  .contact svg { width: 12px; height: 12px; flex: none; }
  .person {
    position: absolute; right: 52px; top: 176px; text-align: right;
  }
  .person-name { font-size: 32px; font-weight: 500; color: var(--accent); letter-spacing: .5px; line-height: 1; }
  .person-title { font-size: 16px; color: var(--ink); letter-spacing: 1px; margin-top: 6px; }
  .address {
    position: absolute; right: 52px; top: 258px;
    text-align: right; font-size: 17px; line-height: 24px; color: var(--ink-soft); font-style: normal;
  }
  .base-band { position: absolute; left: 0; bottom: 0; width: 640px; height: 60px; }
</style>
</head>
<body>

<section class="card card--back" aria-label="Card back">
  <div class="brand-stack">
    <div class="brand-square" aria-hidden="true"></div>
    <p class="brand-name brand-name--large"><span class="word-main">Quillarc</span><span class="word-sub">Laboratories</span></p>
  </div>
  <p class="back-web">www.<span class="highlight">QuillarcWorks</span>.example</p>
</section>

<section class="card card--front" aria-label="Card front">
  <div class="brand-row">
    <div class="brand-square" aria-hidden="true"></div>
    <p class="brand-name brand-name--small"><span class="word-main">Quillarc</span><span class="word-sub">Laboratories</span></p>
  </div>

  <div class="divider"></div>

  <ul class="contact">
    <li>
      <svg viewBox="0 0 12 12" aria-hidden="true"><path d="M3 1 L5 3.5 L4 5 Q5 7 7 8 L8.5 7 L11 9 L9.5 11 Q4 10.5 1 3 Z" fill="var(--accent)"/></svg>
      215 604 8293
    </li>
    <li>
      <svg viewBox="0 0 12 12" aria-hidden="true"><rect x="1" y="2.5" width="10" height="7" fill="none" stroke="var(--accent)" stroke-width="1"/><path d="M1 2.5 L6 6.5 L11 2.5" fill="none" stroke="var(--accent)" stroke-width="1"/></svg>
      JackM@quillarcworks.example
    </li>
    <li>
      <svg viewBox="0 0 12 12" aria-hidden="true"><circle cx="6" cy="6" r="5" fill="none" stroke="var(--accent)" stroke-width="1"/><ellipse cx="6" cy="6" rx="2.2" ry="5" fill="none" stroke="var(--accent)" stroke-width="1"/><path d="M1 6 H11" stroke="var(--accent)" stroke-width="1"/></svg>
      www.QuillarcWorks.example
    </li>
  </ul>

  <div class="person">
    <p class="person-name">JACK MOSS</p>
    <p class="person-title">CEO</p>
  </div>

  <address class="address">2750 Larkmoor Ave<br>Philadelphia PA, 19104</address>

  <svg class="base-band" viewBox="0 0 640 60" aria-hidden="true">
    <path d="M0 6 L330 12 L336 16 L0 12 Z" fill="var(--ink)"/>
    <path d="M0 20 L380 26 C400 26 410 16 440 16 L640 20 L640 60 L0 60 Z" fill="var(--accent)"/>
  </svg>
</section>

</body>
</html>
```